2-Page Flyer for the Information Session about the Tranquil Venture Course

This is a flyer to announce/advertise an evening Information Session about the Tranquil Venture Course. This Program aims at mindfully rethinking and redesigning work (and life) for people who feel stuck or not entirely satisfied with their work and/or life (please see draft flyer attached for more details). This Program is property of Brightfold Joy, a company that uses a combination of Mindfulness, Design, and Entrepreneurship to help people achieve greater happiness (in their work and lives).
Updates

Target Market(s)

People who feel stuck or not entirely satisfied with their work and/or life (please see draft flyer attached for more details)

Font styles to use
Serif
Sans Serif

Colors
ffffff
f37122
33a6d7
acd037

Requirements
Must have
• All of what I will say below is suggestive (I’m not a design expert), and I’m open to divert from it, if it makes sense and feels more interesting.
• I thought initially of a 2-page flyer (please see draft flyer attached). The first page could help people grasp the essence of the event quickly (in 1 or 2 minutes), and then, if they are interested/motivated, they would continue reading through page 2, which has more info about the Program in itself.
• Potential Structure
• Page 1
• . About the Information Session on the Tranquil Venture Course
• . Visible Date & Time, Contacts, Venue (and other relevant info)
• . About me (the facilitator)
• Page 2
• . About the Tranquil Venture Course
• I include a Powerpoint draft of the flyer with the content. The design is rudimentary and precarious from an aesthetics/organization point of view, and this is mainly where I need help (and maybe in other aspects too!).
• On the flyer, I would like to include:
• . A photo of myself (I attach 1 picture).
• . 1 or 2 beautiful-nature photos (cropped or full). One may have to do with looking at the sky, dreaming, and imagining a new work and life (2 photos with sky and clouds attached). The other has to do with walking the transformation journey (the photo with the person walking through the forest path).
• . brightfold joy logo or logos (there are two slightly different ones, that can be used for different purposes). For the first page, I would like the brightfold joy logo that has "brightfold joy" written on the bottom, with the saying "Stillness, Craft and Venture for Joy" beneath. This is the main logo. For the 2nd page, you can choose the logo that adapts better.
• - Where it says the "the way out is in" it would be great to have a similar font to the one I attach (see file "Font_the_way_out_is_in.png" and Ankecallig-fg.ttf
Nice to have
• In terms of colours, I would not divert much from the logo colours (and of course white and black). I would like the flyer to be quite white. Almost like fairy-tale white: the white horse, the white snow, the white of the stars, the white heaven. White could be the base colour. White means peace, tranquillity, calm contentment, a smile.
• And then use the other colours. The green of the mindfulness. The blue of the sky, the dreams. And the orange of the sun, the energy, the fire, the action. And maybe the black for text.
• Where it says the "the way out is in" it would be great to have a similar font to the one I attach (see file "Font_the_way_out_is_in".
• I would like this flyer to be a piece of art, in every possible way. Simple, beautiful, ease, light, peaceful, calm happy. Just like the Tranquil Venture Course and brightfold joy Company that I am creating intends to be. The mission of this Program and Company is to be a designer, a painter (a Picasso) of happier and more fulfilling human lives.
• I am very much looking forward to seeing your proposal(s).

```html
<!DOCTYPE html>
<html lang="en">
<head>
<meta charset="utf-8">
<title>Tranquil Venture Course – Information Session</title>
<link href="https://fonts.googleapis.com/css2?family=Source+Sans+3:wght@400;600;700&family=Dosis:wght@500&family=Poppins:wght@500;600&family=Parisienne&display=swap" rel="stylesheet">
<style>
:root{
  --white:#ffffff;
  --orange:#f37122;
  --blue:#33a6d7;
  --green:#acd037;
  --green-dark:#8cb82a;
  --ink:#1e1e1e;
}
*{margin:0;padding:0;box-sizing:border-box}
html,body{width:1200px;height:848px;overflow:hidden;background:var(--white)}
body{font-family:"Source Sans 3",Arial,sans-serif;color:var(--ink)}
.flyer{position:relative;width:1200px;height:848px;overflow:hidden;background:var(--white)}
.shapes{position:absolute;inset:0}
.abs{position:absolute}

/* brand */
.brand{left:70px;top:22px;width:180px;text-align:center}
.brand-dot{width:62px;height:62px;border-radius:50%;background:var(--blue);margin:0 auto 10px}
.brand-name{font-size:25px;font-weight:400;color:var(--blue);line-height:1}
.brand-tagline{font-size:8.5px;color:var(--green-dark);margin-top:6px;line-height:1.2}

.title{left:275px;top:30px;font-family:"Dosis",sans-serif;font-weight:500;font-size:32px;line-height:34px;letter-spacing:.3px}
.title .t-blue{color:var(--blue)}
.title .t-orange{color:var(--orange)}

/* left page */
.session-head{left:90px;top:164px;font-size:17px;font-weight:700;color:var(--green-dark)}
.session-text{left:90px;top:188px;width:410px;font-size:15.5px;line-height:17.5px}
.fac-head{left:90px;top:272px;font-size:17px;font-weight:700;color:var(--green-dark)}
.fac-name{left:90px;top:293px;font-size:12.5px}
.fac-name b{color:var(--blue)}
.fac-bio{left:90px;top:320px;width:422px;font-size:12.8px;line-height:14.8px;text-align:justify}
.more{left:90px;top:545px;font-size:12.5px}
.more span{color:var(--orange)}
.contact{left:90px;top:577px;font-size:12.5px;line-height:15.5px}

.date{left:82px;top:700px;transform:rotate(13deg);transform-origin:left top;font-family:"Poppins",sans-serif;font-weight:500;font-size:23px;line-height:30px;color:var(--white);letter-spacing:.5px}
.date .time{display:block;margin-left:-14px}

/* right page */
.bar{background:var(--orange);color:var(--white);font-weight:700;font-size:13px;height:26px;line-height:26px;text-align:center}
.bar-what{left:595px;top:20px;width:270px}
.bar-how{left:865px;top:20px;width:265px}
.bar-why{left:595px;top:181px;width:233px}
.bar-program{left:595px;top:421px;width:183px}
.copy{font-size:10px;line-height:13.6px;text-align:justify}
.copy-what{left:620px;top:58px;width:234px}
.copy-how{left:884px;top:58px;width:254px}
.copy-why{left:620px;top:232px;width:234px}
.aims-head{color:var(--orange);font-weight:700;font-size:11px;margin-top:2px}
.aims{list-style:none}
.copy-program{left:617px;top:456px;width:190px}
.curve-wrap{float:right;width:190px;height:260px;
  shape-outside:polygon(170px 0,161px 104px,121px 164px,76px 224px,60px 260px,190px 260px,190px 0)}

.quote{left:828px;top:490px;font-family:"Parisienne",cursive;font-size:42px;color:var(--ink);white-space:nowrap}
.portrait{left:980px;top:632px;width:200px;height:200px;border-radius:50%;background:var(--white);border:10px solid var(--orange);padding:7px}
.portrait-fill{width:100%;height:100%;border-radius:50%;background:radial-gradient(circle at 50% 40%,#d9d6d3,#a7a9ac)}
.right-contact{left:790px;top:756px;width:180px;color:var(--white);font-family:"Poppins",sans-serif;font-weight:600;font-size:10.5px;line-height:20px;text-align:right}
.right-dot{left:1160px;top:20px;width:22px;height:22px;border-radius:50%;background:var(--blue)}
</style>
</head>
<body>
<main class="flyer">
  <svg class="shapes" width="1200" height="848" viewBox="0 0 1200 848">
    <defs>
      <linearGradient id="skyGrad" x1="0" y1="0" x2="0" y2="1">
        <stop offset="0" stop-color="#4a86cc"/>
        <stop offset=".4" stop-color="#b9d6ee"/>
        <stop offset=".55" stop-color="#e3ecf3"/>
        <stop offset=".68" stop-color="#7a977f"/>
        <stop offset="1" stop-color="#3f6a57"/>
      </linearGradient>
      <linearGradient id="seaGrad" x1="0" y1="0" x2="1" y2="1">
        <stop offset="0" stop-color="#2f9fd6"/>
        <stop offset="1" stop-color="#4bb3e3"/>
      </linearGradient>
    </defs>
    <path role="img" aria-label="Photo of a blue sky with white clouds over green mountain ridges"
      d="M1200 230 C1060 260 920 340 860 430 C800 520 740 620 690 700 C660 760 640 800 625 848 L1200 848 Z" fill="url(#skyGrad)"/>
    <path d="M1200 220 C1055 250 912 332 850 425 C790 515 730 615 680 695 C650 755 630 800 612 848 L625 848 C640 800 660 760 690 700 C740 620 800 520 860 430 C920 340 1060 260 1200 230 Z" fill="var(--green)"/>
    <path d="M0 655 C150 690 380 690 600 650 L600 848 L0 848 Z" fill="url(#seaGrad)"/>
    <path d="M0 700 C170 700 390 650 600 560 L600 600 C400 680 180 712 0 712 Z" fill="var(--green)"/>
  </svg>

  <div class="abs brand">
    <div class="brand-dot"></div>
    <div class="brand-name">brightfold joy</div>
    <div class="brand-tagline">“Stillness, Craft and Venture for Joy”</div>
  </div>

  <h1 class="abs title">
    <span class="t-blue">TRANQUIL</span><br>
    <span class="t-orange">VENTURE</span><br>
    <span class="t-blue">COURSE</span>
  </h1>

  <h2 class="abs session-head">INFORMATION SESSION</h2>
  <p class="abs session-text">The purpose of this Information Session is to give you a real insight into the Tranquil Venture Course and how it can help you make the most of your professional and personal life.</p>

  <h2 class="abs fac-head">FACILITATOR:</h2>
  <p class="abs fac-name"><b>Dr Marco Vale</b>, Visiting Research Fellow, University of Wexmoor</p>
  <p class="abs fac-bio"><b>Marco</b> joined the University of Wexmoor (School of Management) as a Lecturer in Entrepreneurship in 2015. He completed his PhD in Entrepreneurship at Harbourside Business School in 2014. His work received the Linden Doctoral Thesis Prize from the Guild of Management Scholars. He began his business career as a production engineer (Voltrix), and continued in sales (Kernwerk). After his MBA, he worked as a strategy consultant at Riverton Business School. Originally from Portugal, Marco enjoys designing and launching new ideas, international communities, mindfulness retreats, and musical improvisation. He nurtures a close connection to Quiet Meadow Practice Centre, where he has practiced and volunteered over 9 months. He has a broad experience of sharing the benefits of mindfulness with others.</p>

  <p class="abs more">More about the facilitator: <span>www.profilehub.net/marcovale</span></p>
  <p class="abs contact">Information &amp; Booking Email: hello@brightfoldjoy.example<br>Tel: +34 600 000 123 (video call and messaging)<br>Venue: Lantern Coworking, C/ del Olmo 12, Barcelona</p>

  <p class="abs date">Thursday 5th September 2019<span class="time">19:30 to 21:00</span></p>

  <div class="abs bar bar-what">What is Tranquil Venture</div>
  <div class="abs bar bar-how">HOW</div>
  <div class="abs right-dot"></div>

  <p class="abs copy copy-what">Being mindful means being aware and awake. Entrepreneurship is the creation of a new form of organising. Tranquil Venture is then the process of creating or redesigning your work and life with awareness, in a way that is reflective of you, of your passions and values, thus conducing to a greater sense of fulfilment and happiness.</p>

  <p class="abs copy copy-how">This Program differs from existing entrepreneurial programs in many ways: 1) Uses mindfulness and self analysis to look deeply into yourself<br>2) Design and execution decisions are based on happiness rather than (only) financials<br>3) Holistic and inclusive design process, integrating work and life, and building synergies between your different parts.<br>The Program format includes lectures, individual work, group sharing, guided activities, experiential exercises, video, audio, handouts and other resources.</p>

  <div class="abs bar bar-why">WHY</div>
  <div class="abs copy copy-why">
    <p>Many people are not satisfied with their work or life, but they don’t know what to do about it. This Program offers you a safe place to conduct your inner journey with collective support, helping you reflect, design, and (very likely) do something about it.</p>
    <p class="aims-head">It aims at:</p>
    <ul class="aims">
      <li>1) Increasing awareness, clarity and confidence</li>
      <li>2) Having a deeper insight on what makes you happier and what you want</li>
      <li>3) Developing a clear design integrating your intended work and life</li>
      <li>4) Start executing this design.</li>
    </ul>
  </div>

  <div class="abs bar bar-program">THE PROGRAM</div>
  <div class="abs copy copy-program"><span class="curve-wrap"></span>The Tranquil Venture Course is a 4-month long transformative journey designed for people who feel stuck or not entirely satisfied with their professional and/or personal life. It will be of benefit for everyone, at any stage. The Program consists of a 5-hour workshop every month, complemented by 2-hour weekly peer-support meetings. It combines mindfulness techniques, design thinking methodology, and entrepreneurship frameworks.</div>

  <p class="abs quote">“The way out is in”</p>

  <p class="abs right-contact">Email: hello@brightfoldjoy.example<br>Tel: +34 600 000 123<br>(video call and messaging)</p>

  <div class="abs portrait">
    <div class="portrait-fill" role="img" aria-label="Portrait photo of the facilitator"></div>
  </div>
</main>
</body>
</html>
```